Urine collection cup with and without sterile seal sticker

Hello. We need a urine cup label designed please with

Name:
Date of Birth:
Date:
Time:
Temp℃:
Specimen ID:

Product code: TUB-47
Volume markings (e.g., 30 mL, 60 mL, 90 mL).
Vela Drug Tests logo

Could you please provide one version with the additional sterile sticker extending to the top, and one version without the additional sterile sticker?

```html
<!DOCTYPE html>
<html lang="en">
<head>
<meta charset="utf-8">
<title>Vela Drug Tests – Urine Cup Labels</title>
<link href="https://fonts.googleapis.com/css2?family=Arimo:wght@400;600;700&display=swap" rel="stylesheet">
<style>
  :root {
    --navy: #13294f;
    --orange: #f7731c;
    --peach: #f6c6aa;
    --tint: #fde9dc;
    --grey-band: #e8e8e8;
    --grey-hint: #d3d7de;
    --white: #ffffff;
  }
  html, body {
    margin: 0;
    padding: 0;
    width: 1200px;
    height: 800px;
    overflow: hidden;
    background: var(--white);
  }
  .label-sheet {
    display: block;
    width: 1200px;
    height: 800px;
    font-family: "Arimo", Arial, sans-serif;
  }
  .card-frame { fill: var(--white); stroke: var(--navy); stroke-width: 3; }
  .card-outline { fill: none; stroke: var(--navy); stroke-width: 3; }
  .band-navy { fill: var(--navy); }
  .band-orange { fill: var(--orange); }
  .band-grey { fill: var(--grey-band); }
  .corner-tint { fill: url(#corner-tint); }
  .brand-mark { fill: var(--orange); }
  .brand-name { fill: var(--navy); font-size: 40px; font-weight: 700; }
  .field-icon-bg { fill: var(--navy); }
  .field-label { fill: var(--navy); font-size: 22px; font-weight: 600; }
  .field-line { stroke: var(--navy); stroke-width: 1.4; }
  .hint { font-size: 17px; font-weight: 400; }
  .hint-peach { fill: var(--peach); }
  .hint-grey { fill: var(--grey-hint); }
  .hint-line-peach { stroke: var(--peach); stroke-width: 1.4; }
  .slash { fill: var(--navy); font-size: 21px; font-weight: 600; }
  .scale-line { stroke: var(--navy); stroke-width: 2; fill: none; }
  .scale-text { fill: var(--navy); font-size: 21px; font-weight: 700; }
  .code-caption { fill: var(--white); font-size: 22px; font-weight: 600; }
  .code-value { fill: var(--white); font-size: 44px; font-weight: 700; }
  .thanks-light { fill: var(--white); font-size: 22px; font-weight: 600; }
  .thanks-dark { fill: var(--navy); font-size: 22px; font-weight: 600; }
  .flask-light { fill: none; stroke: var(--white); stroke-width: 2.2; }
  .flask-dark { fill: none; stroke: var(--navy); stroke-width: 2.2; }
  .seal-strip { fill: var(--navy); }
  .seal-title { fill: var(--white); font-size: 22px; font-weight: 700; }
  .seal-tick { fill: none; stroke: var(--white); stroke-width: 3; }
  .seal-perforation { stroke: var(--white); stroke-width: 2.5; stroke-dasharray: 11 8; }
  .seal-note { fill: var(--white); font-size: 19px; font-weight: 700; }
</style>
</head>
<body>
<svg class="label-sheet" viewBox="0 0 1536 1024" xmlns="http://www.w3.org/2000/svg">
  <defs>
    <clipPath id="card-clip-sealed"><rect x="43" y="115" width="697" height="830" rx="40"/></clipPath>
    <clipPath id="card-clip-plain"><rect x="797" y="115" width="697" height="830" rx="40"/></clipPath>
    <linearGradient id="corner-tint" x1="1" y1="0" x2="0" y2="1">
      <stop offset="0" stop-color="#fde9dc"/>
      <stop offset="1" stop-color="#ffffff"/>
    </linearGradient>

    <g id="icon-person">
      <circle r="23" class="field-icon-bg"/>
      <circle cy="-5" r="5.5" fill="#fff"/>
      <path d="M-10,9 Q-10,1 0,1 Q10,1 10,9 Z" fill="#fff"/>
    </g>
    <g id="icon-calendar">
      <circle r="23" class="field-icon-bg"/>
      <rect x="-11" y="-10" width="22" height="20" rx="2" fill="#fff"/>
      <rect x="-11" y="-10" width="22" height="5" fill="#13294f" opacity="0.35"/>
      <path d="M-7,-2 H7 M-7,3 H7 M-3,-4 V8 M2,-4 V8" stroke="#13294f" stroke-width="1.2"/>
    </g>
    <g id="icon-date">
      <circle r="23" class="field-icon-bg"/>
      <rect x="-12" y="-10" width="21" height="19" rx="2" fill="#fff"/>
      <path d="M-8,-2 H6 M-8,3 H6 M-4,-4 V8 M1,-4 V8" stroke="#13294f" stroke-width="1.2"/>
      <circle cx="8" cy="8" r="5" fill="#fff" stroke="#13294f" stroke-width="1.4"/>
    </g>
    <g id="icon-clock">
      <circle r="23" class="field-icon-bg"/>
      <circle r="13" fill="#fff"/>
      <circle r="10.5" fill="none" stroke="#13294f" stroke-width="1.2"/>
      <path d="M0,-7 V0 L5,3" fill="none" stroke="#13294f" stroke-width="1.8"/>
    </g>
    <g id="icon-thermo">
      <circle r="23" class="field-icon-bg"/>
      <rect x="-5" y="-13" width="8" height="18" rx="4" fill="#fff"/>
      <circle cx="-1" cy="8" r="6" fill="#fff"/>
      <path d="M6,-9 H10 M6,-5 H9 M6,-1 H10" stroke="#fff" stroke-width="1.5"/>
    </g>
    <g id="icon-id">
      <circle r="23" class="field-icon-bg"/>
      <rect x="-12" y="-8" width="24" height="17" rx="2" fill="none" stroke="#fff" stroke-width="2"/>
      <rect x="-8" y="-4" width="7" height="8" fill="#fff"/>
      <path d="M2,-3 H9 M2,1 H9 M2,5 H7" stroke="#fff" stroke-width="1.5"/>
    </g>
    <g id="flask-shape">
      <path d="M-7,-30 H7 M-5,-30 V-12 L-22,16 Q-24,22 -17,22 H17 Q24,22 22,16 L5,-12 V-30"/>
      <path d="M-14,4 H14"/>
      <circle cx="-8" cy="13" r="3"/>
      <circle cx="4" cy="15" r="2"/>
      <circle cx="10" cy="9" r="2"/>
    </g>
  </defs>

  <!-- Label with sterile seal -->
  <g class="label label-sealed">
    <rect class="card-frame" x="43" y="115" width="697" height="830" rx="40"/>
    <g clip-path="url(#card-clip-sealed)">
      <rect class="corner-tint" role="img" aria-label="Decorative pattern area"
            x="285" y="116" width="275" height="165"/>
      <path class="band-navy" d="M40,820 L420,848 L330,948 L40,948 Z"/>
      <path class="band-orange" d="M312,948 L392,860 Q410,840 440,840 L745,840 L745,948 Z"/>
    </g>
    <rect class="card-outline" x="43" y="115" width="697" height="830" rx="40"/>

    <g class="brand">
      <circle class="brand-mark" cx="128" cy="210" r="34"/>
      <text class="brand-name" x="178" y="224">Vela Drug Tests</text>
    </g>

    <g class="fields">
      <use href="#icon-person" x="93" y="348"/>
      <text class="field-label" x="132" y="356">Name:</text>
      <line class="field-line" x1="213" y1="365" x2="537" y2="365"/>

      <use href="#icon-calendar" x="93" y="428"/>
      <text class="field-label" x="132" y="435">Date of Birth:</text>
      <text class="hint hint-peach" x="314" y="437" text-anchor="middle">DD</text>
      <line class="hint-line-peach" x1="286" y1="443" x2="341" y2="443"/>
      <text class="slash" x="356" y="447" text-anchor="middle">/</text>
      <text class="hint hint-peach" x="405" y="437" text-anchor="middle">MM</text>
      <line class="hint-line-peach" x1="378" y1="443" x2="433" y2="443"/>
      <text class="slash" x="446" y="447" text-anchor="middle">/</text>
      <text class="hint hint-peach" x="497" y="437" text-anchor="middle">YYYY</text>
      <line class="field-line" x1="457" y1="443" x2="537" y2="443"/>

      <use href="#icon-date" x="93" y="507"/>
      <text class="field-label" x="132" y="515">Date:</text>
      <line class="field-line" x1="200" y1="523" x2="537" y2="523"/>

      <use href="#icon-clock" x="93" y="587"/>
      <text class="field-label" x="132" y="595">Time:</text>
      <text class="hint hint-peach" x="466" y="598" text-anchor="middle">AM</text>
      <text class="slash" x="494" y="599" text-anchor="middle" font-size="18">/</text>
      <text class="hint hint-peach" x="520" y="598" text-anchor="middle">PM</text>
      <line class="field-line" x1="203" y1="603" x2="537" y2="603"/>

      <use href="#icon-thermo" x="93" y="667"/>
      <text class="field-label" x="132" y="675">Temp°C:</text>
      <line class="field-line" x1="234" y1="684" x2="537" y2="684"/>

      <use href="#icon-id" x="93" y="747"/>
      <text class="field-label" x="132" y="755">Specimen ID:</text>
      <line class="field-line" x1="288" y1="764" x2="537" y2="764"/>
    </g>

    <g class="volume-scale">
      <path class="scale-line" d="M640,327 V653 M630,327 H656 M630,490 H656 M630,653 H656"/>
      <text class="scale-text" x="658" y="328">90 ML</text>
      <text class="scale-text" x="658" y="491">60 ML</text>
      <text class="scale-text" x="658" y="654">30 ML</text>
    </g>

    <g class="product-code">
      <text class="code-caption" x="72" y="870">Product code  :</text>
      <text class="code-value" x="72" y="915">TUB-47</text>
    </g>
    <g class="thanks">
      <use href="#flask-shape" x="475" y="893" class="flask-light"/>
      <text class="thanks-light" x="518" y="882">Thank you for</text>
      <text class="thanks-light" x="518" y="909">your cooperation.</text>
    </g>

    <g class="sterile-seal">
      <path class="seal-strip" d="M543,63 H636 Q656,63 656,83 V185 Q656,205 640,215 Q627,225 627,240 V820 Q627,833 614,833 H566 Q553,833 553,820 V240 Q553,225 540,215 Q523,205 523,185 V83 Q523,63 543,63 Z"/>
      <text class="seal-title" x="592" y="104" text-anchor="middle">STERILE</text>
      <circle class="seal-tick" cx="593" cy="150" r="24"/>
      <path class="seal-tick" d="M582,151 L590,159 L605,142"/>
      <line class="seal-perforation" x1="540" y1="200" x2="648" y2="200"/>
      <text class="seal-note" transform="translate(585,529) rotate(90)" text-anchor="middle" textLength="492" lengthAdjust="spacingAndGlyphs">INTERIOR AS LONG AS SEAL REMAINS INTACT</text>
    </g>
  </g>

  <!-- Label without sterile seal -->
  <g class="label label-plain">
    <rect class="card-frame" x="797" y="115" width="697" height="830" rx="40"/>
    <g clip-path="url(#card-clip-plain)">
      <rect class="corner-tint" role="img" aria-label="Decorative pattern area"
            x="1150" y="116" width="346" height="170"/>
      <path class="band-navy" d="M794,820 L1174,848 L1084,948 L794,948 Z"/>
      <path class="band-grey" d="M1066,948 L1146,860 Q1164,840 1194,840 L1499,840 L1499,948 Z"/>
    </g>
    <rect class="card-outline" x="797" y="115" width="697" height="830" rx="40"/>

    <g class="brand">
      <circle class="brand-mark" cx="882" cy="210" r="34"/>
      <text class="brand-name" x="932" y="224">Vela Drug Tests</text>
    </g>

    <g class="fields">
      <use href="#icon-person" x="847" y="348"/>
      <text class="field-label" x="886" y="356">Name:</text>
      <line class="field-line" x1="967" y1="365" x2="1312" y2="365"/>

      <use href="#icon-calendar" x="847" y="428"/>
      <text class="field-label" x="886" y="435">Date of Birth:</text>
      <text class="hint hint-grey" x="1068" y="437" text-anchor="middle">DD</text>
      <line class="field-line" x1="1040" y1="443" x2="1095" y2="443"/>
      <text class="slash" x="1110" y="447" text-anchor="middle">/</text>
      <text class="hint hint-grey" x="1159" y="437" text-anchor="middle">MM</text>
      <line class="field-line" x1="1132" y1="443" x2="1187" y2="443"/>
      <text class="slash" x="1200" y="447" text-anchor="middle">/</text>
      <text class="hint hint-grey" x="1270" y="437" text-anchor="middle">YYYY</text>
      <line class="field-line" x1="1226" y1="443" x2="1312" y2="443"/>

      <use href="#icon-date" x="847" y="507"/>
      <text class="field-label" x="886" y="515">Date:</text>
      <line class="field-line" x1="954" y1="523" x2="1312" y2="523"/>

      <use href="#icon-clock" x="847" y="587"/>
      <text class="field-label" x="886" y="595">Time:</text>
      <text class="hint hint-grey" x="1239" y="598" text-anchor="middle">AM</text>
      <text class="hint hint-grey" x="1266" y="598" text-anchor="middle">/</text>
      <text class="hint hint-grey" x="1293" y="598" text-anchor="middle">PM</text>
      <line class="field-line" x1="957" y1="603" x2="1312" y2="603"/>

      <use href="#icon-thermo" x="847" y="667"/>
      <text class="field-label" x="886" y="675">Temp°C:</text>
      <line class="field-line" x1="988" y1="684" x2="1312" y2="684"/>

      <use href="#icon-id" x="847" y="747"/>
      <text class="field-label" x="886" y="755">Specimen ID:</text>
      <line class="field-line" x1="1047" y1="764" x2="1312" y2="764"/>
    </g>

    <g class="volume-scale">
      <path class="scale-line" d="M1394,327 V653 M1384,327 H1410 M1384,490 H1410 M1384,653 H1410"/>
      <text class="scale-text" x="1412" y="328">90 ML</text>
      <text class="scale-text" x="1412" y="491">60 ML</text>
      <text class="scale-text" x="1412" y="654">30 ML</text>
    </g>

    <g class="product-code">
      <text class="code-caption" x="826" y="870">Product code  :</text>
      <text class="code-value" x="826" y="915">TUB-47</text>
    </g>
    <g class="thanks">
      <use href="#flask-shape" x="1229" y="893" class="flask-dark"/>
      <text class="thanks-dark" x="1272" y="882">Thank you for</text>
      <text class="thanks-dark" x="1272" y="909">your cooperation.</text>
    </g>
  </g>
</svg>
</body>
</html>
```